Flyer-Design für Immobilienbüro
Zielgruppe
Wir sind ein Immobilienbüro. Es sollen Immobilienverkäufer angesprochen werden um uns zu beauftragen Ihre Immobilie zu verkaufen. Motto sollte sein: ' Immobilienverkauf ist stressig. JA. Aber nicht für Sie '.
Aufgabenstellung
DIN A5 hochkant. beidseitig bedruckt. auf Rückseite unten soll Antwortkarte an uns adressiert sein sein.
Es sollen Immobilienverkäufer angesprochen werden um uns zu beauftragen Ihre Immobilie zu verkaufen. Motto sollte sein: ' Immobilienverkauf ist stressig. JA. Aber nicht für Sie '.
(Dies sollte auch durch ein Bild dargestellt werden)
Rundum-Sorglos Immobilienverkauf - 100% kostenlos für Sie als Eigentümer
es sollte auf dem Flyer vermerkt sein:
- Unser Service ist für Sie als Verkäufer 100 % KOSTENLOS
- bei einer Beauftragung erhalten Sie den Energieausweis von uns KOSTENLOS
- wir besorgen alle zum Verkauf benötigter Dokumente für Sie KOSTENLOS
- wir sind ständig auf der Suche nach Objekten die wir selbst ankaufen. Kaufentscheidung innerhalb von 2 Tagen.
- FÜR TIPPGEBER: Sie kennen jemanden, der eine Immobilie zu verkaufen hat? Tippgeber erhalten bis zu 5.000,- Euro Provision in Bar. Kontraktieren Sie uns.
Design soll hochwertig und elegant sein.
Als Kontakttelefonnummer soll diese vermerkt sein.
Antwortkarte auf der Rückseite sollte Antworttext in etwa enthalten:
O Wir haben eine Immobile zu verkaufen. Rufen Sie uns bitte an
O Wir haben demnächst eine Immobilien zu verkaufen. Rufen Sie uns bitte an.
O Ich kenne jemanden der seine Immobilie verkauft und möchte Tipgeber sein
Name / Vorname
Straße / PLZ / Ort
Telefonnummer

```html
<!DOCTYPE html>
<html lang="de">
<head>
<meta charset="utf-8">
<title>Flyer Immobilien Haller &amp; Brenner</title>
<link href="https://fonts.googleapis.com/css2?family=Lato:wght@400;700;900&family=Crimson+Pro:wght@400&display=swap" rel="stylesheet">
<style>
  :root {
    --bg: #ececec;
    --paper: #ffffff;
    --green: #3b6a27;
    --green-dark: #1c4a2a;
    --green-band: #3f6a2c;
    --gold: #c4a03a;
    --text-dark: #2d2d2d;
    --grey-light: #e3e3e3;
  }
  * { box-sizing: border-box; margin: 0; padding: 0; }
  html, body { width: 1200px; height: 848px; overflow: hidden; }
  body { background: var(--bg); font-family: "Lato", Arial, sans-serif; position: relative; }

  .page { position: absolute; top: 29px; width: 552px; height: 783px; background: var(--paper); overflow: hidden; }
  .page--front { left: 38px; background: linear-gradient(#f3f3f3, #dcdcdc); }
  .page--back { left: 620px; }

  /* Front */
  .hero-photo { position: absolute; left: 0; top: 0; width: 552px; height: 430px;
    background: linear-gradient(160deg, #f7f7f5 0%, #eeeae4 45%, #d9c2a2 80%, #cfb797 100%); }
  .front-frame { position: absolute; left: 28px; top: 31px; width: 496px; height: 715px; border: 2px solid var(--gold); }
  .brand-box { position: absolute; left: 302px; top: 0; width: 202px; height: 118px; background: var(--green-dark);
    display: flex; flex-direction: column; align-items: center; justify-content: center; gap: 8px; }
  .brand-box__mark { width: 14px; height: 14px; border-radius: 50%; background: var(--gold); }
  .brand-box__name { color: #fff; font-size: 11px; letter-spacing: 2px; font-weight: 400; text-align: center; line-height: 1.5; }

  .headline { position: absolute; left: 47px; top: 395px; color: var(--green); }
  .headline__ja { font-size: 66px; font-weight: 900; line-height: 1; color: #2f5a1e; }
  .headline__line { font-size: 31px; font-weight: 900; line-height: 1.22; }

  .band { position: absolute; left: 0; top: 608px; width: 552px; height: 98px; background: var(--green-band); }
  .band-house { position: absolute; left: 44px; top: 569px; }
  .band-text { position: absolute; left: 45px; top: 618px; color: #fff; font-size: 15px; line-height: 1.25; }
  .band-text strong { font-size: 19px; font-weight: 900; display: block; margin-top: 2px; }

  .team-photo { position: absolute; left: 205px; top: 549px; width: 347px; height: 234px;
    background: linear-gradient(180deg, #5a5a5a 0%, #2c2c2e 60%, #1e1e20 100%); }
  .team-claim { position: absolute; left: 360px; top: 686px; color: #fff; font-size: 15px; font-weight: 700; line-height: 1.2; }
  .team-underline { position: absolute; left: 360px; top: 745px; width: 164px; height: 3px; background: var(--gold); }
  .chat-icon { position: absolute; left: 485px; top: 669px; }

  /* Back */
  .city-photo { position: absolute; left: 0; top: 0; width: 552px; height: 159px;
    background: linear-gradient(180deg, #b9c9d6 0%, #9aa79a 30%, #a4673e 65%, #6d6a48 100%); }
  .back-brand { position: absolute; left: 28px; top: 12px; display: flex; align-items: center; gap: 7px;
    color: var(--gold); font-size: 12px; font-weight: 700; letter-spacing: 1.5px; }
  .back-brand__mark { width: 10px; height: 10px; border-radius: 50%; background: var(--gold); }
  .back-frame { position: absolute; left: 25px; top: 45px; width: 506px; height: 320px; border: 2px solid var(--gold); }

  .benefits { position: absolute; top: 176px; list-style: none; color: var(--green); font-size: 11.8px; font-weight: 700; line-height: 1.25; }
  .benefits li { position: relative; padding-left: 10px; margin-bottom: 13px; }
  .benefits li::before { content: "•"; position: absolute; left: 0; top: 0; }
  .benefits--left { left: 44px; width: 236px; }
  .benefits--right { left: 290px; width: 236px; }

  .contact-icon { position: absolute; left: 46px; top: 316px; }
  .contact { position: absolute; left: 93px; top: 313px; color: var(--green); font-size: 11.5px; line-height: 1.3; }
  .contact b { font-weight: 700; }

  .cut-line { position: absolute; left: 0; top: 390px; width: 552px; border-top: 1.5px dashed #333; }
  .scissors { position: absolute; left: 22px; top: 383px; }

  .privacy { position: absolute; left: 16px; top: 733px; width: 280px; transform: rotate(-90deg); transform-origin: 0 0;
    font-size: 6px; line-height: 1.3; color: var(--text-dark); }

  .reply-title { position: absolute; left: 58px; top: 444px; color: var(--green); font-size: 12px; font-weight: 700; }
  .reply-options { position: absolute; left: 57px; top: 472px; list-style: none; font-size: 11.5px; color: var(--text-dark); line-height: 1.25; width: 260px; }
  .reply-options li { position: relative; padding-left: 12px; margin-bottom: 15px; }
  .reply-options li::before { content: ""; position: absolute; left: 0; top: 3px; width: 8px; height: 8px; border: 1.2px solid #333; border-radius: 50%; }

  .field { position: absolute; left: 56px; width: 250px; border-top: 1px solid #b9b9b9; font-size: 10.5px; color: var(--text-dark); padding-top: 2px; }

  .card-divider { position: absolute; left: 325px; top: 445px; width: 1.5px; height: 290px; background: var(--green); }
  .stamp-box { position: absolute; left: 450px; top: 449px; width: 63px; height: 81px; border: 1.5px solid #222;
    display: flex; align-items: center; justify-content: center; text-align: center; font-size: 9px; line-height: 1.4; color: #222; }
  .postal-service { position: absolute; left: 345px; top: 554px; font-size: 8.5px; font-weight: 700; color: #111; line-height: 1.5; }
  .postal-service i { font-weight: 900; }
  .recipient-brand { position: absolute; left: 345px; top: 594px; display: flex; align-items: center; gap: 8px;
    color: var(--gold); font-size: 13px; font-weight: 700; letter-spacing: 1.5px; }
  .recipient-brand__mark { width: 12px; height: 12px; border-radius: 50%; background: var(--gold); }
  .recipient-address { position: absolute; left: 345px; top: 622px; font-family: "Crimson Pro", Georgia, serif; font-size: 13px; line-height: 1.3; color: #222; }
  .recipient-address .city { margin-top: 15px; }
</style>
</head>
<body>

<!-- Front side -->
<section class="page page--front">
  <div class="hero-photo" role="img" aria-label="Hand hält ein Modellhaus mit Schlüssel, dahinter ein entspanntes Paar in einer hellen leeren Wohnung"></div>
  <div class="front-frame"></div>
  <div class="brand-box">
    <span class="brand-box__mark"></span>
    <span class="brand-box__name">IMMOBILIEN<br>HALLER &amp; BRENNER</span>
  </div>

  <div class="headline">
    <div class="headline__ja">JA,</div>
    <div class="headline__line">Immobilienverkauf ist stressig!</div>
    <div class="headline__line">Aber nicht für Sie.</div>
  </div>

  <svg class="band-house" width="130" height="40" viewBox="0 0 130 40" aria-hidden="true">
    <path d="M0 20 L32 6 L64 20 L64 40 L0 40 Z M64 26 L88 14 L112 26 L112 40 L64 40 Z" fill="var(--green-band)"/>
  </svg>
  <div class="band"></div>
  <div class="band-text">
    Rundum-Sorglos<br>Immobilienverkauf.
    <strong>100% kostenlos</strong>
    für Sie als Eigentümer.
  </div>

  <div class="team-photo" role="img" aria-label="Drei Makler in dunklen Anzügen als Team-Porträt"></div>
  <svg class="chat-icon" width="38" height="34" viewBox="0 0 38 34" aria-hidden="true">
    <path d="M3 2 H35 V24 H16 L8 32 V24 H3 Z" fill="var(--gold)"/>
    <path d="M12 14 L19 8 L26 14 V20 H12 Z" fill="#222"/>
    <rect x="17" y="15" width="4" height="5" fill="var(--gold)"/>
  </svg>
  <div class="team-claim">Wir vermitteln<br>Ihre Immobilie zum<br>Höchstpreis.</div>
  <div class="team-underline"></div>
</section>

<!-- Back side -->
<section class="page page--back">
  <div class="city-photo" role="img" aria-label="Stadtpanorama mit Dächern und grünen Kirchturmkuppeln"></div>
  <div class="back-brand"><span class="back-brand__mark"></span>IMMOBILIEN HALLER &amp; BRENNER</div>
  <div class="back-frame"></div>

  <ul class="benefits benefits--left">
    <li>Unser Service ist für Sie als Verkäufer 100 % KOSTENLOS.</li>
    <li>Bei einer Beauftragung erhalten Sie den Energieausweis von uns KOSTENLOS.</li>
    <li>Wir besorgen alle zum Verkauf benötigter Dokumente für Sie KOSTENLOS.</li>
  </ul>
  <ul class="benefits benefits--right">
    <li>Wir sind auch ständig auf der Suche nach Objekten die wir selbst ankaufen. Kaufentscheidung innerhalb von 2 Tagen.</li>
    <li>FÜR TIPPGEBER: Sie kennen jemanden, der eine Immobilie zu verkaufen hat? Tippgeber erhalten bis zu 5.000,- Euro Provision in Bar. Kontraktieren Sie uns.</li>
  </ul>

  <svg class="contact-icon" width="38" height="34" viewBox="0 0 38 34" aria-hidden="true">
    <path d="M1 1 H37 V24 H18 L10 33 V24 H1 Z" fill="var(--gold)"/>
    <path d="M11 14 L19 7 L27 14 V21 H11 Z" fill="#fff"/>
    <rect x="17" y="15" width="4" height="6" fill="var(--gold)"/>
  </svg>
  <div class="contact">
    Immobilien Haller &amp; Brenner GbR &nbsp;•&nbsp; Lindenweg 8 &nbsp;•&nbsp; 86999 Musterhausen<br>
    <b>Mob. 0170-5550123 &nbsp;•&nbsp; Tel. 08200-5550-10 oder -11</b><br>
    www.haller-brenner.de &nbsp;•&nbsp; info@haller-brenner.de
  </div>

  <div class="cut-line"></div>
  <svg class="scissors" width="24" height="14" viewBox="0 0 24 14" aria-hidden="true">
    <rect x="0" y="0" width="24" height="14" fill="#fff"/>
    <circle cx="4" cy="3.5" r="2.6" fill="none" stroke="#222" stroke-width="1.4"/>
    <circle cx="4" cy="10.5" r="2.6" fill="none" stroke="#222" stroke-width="1.4"/>
    <path d="M6 5 L22 11 M6 9 L22 3" stroke="#222" stroke-width="1.4"/>
  </svg>

  <p class="privacy">Mit der Zusendung Ihrer Daten erklären Sie sich mit der Kontaktaufnahme einverstanden. Die Datenschutzerklärung finden Sie hier: www.haller-brenner.de/datenschutz</p>

  <div class="reply-title">Wir freuen uns auf Ihre Kontaktaufnahme</div>
  <ul class="reply-options">
    <li>Wir haben eine Immobilie zu verkaufen.<br>Rufen Sie uns bitte an.</li>
    <li>Wir haben demnächst eine Immobilien<br>zu verkaufen. Rufen Sie uns bitte an.</li>
    <li>Ich kenne jemanden der seine Immobilie<br>verkauft und möchte Tippgeber sein.</li>
  </ul>

  <div class="field" style="top:626px">Name / Vorname</div>
  <div class="field" style="top:659px">Straße</div>
  <div class="field" style="top:691px">PLZ / Ort</div>
  <div class="field" style="top:723px">Telefonnummer</div>

  <div class="card-divider"></div>
  <div class="stamp-box">Entgelt<br>zahlt<br>Empfänger</div>
  <div class="postal-service">Briefdienst<br><i>ANTWORT</i></div>
  <div class="recipient-brand"><span class="recipient-brand__mark"></span>HALLER &amp; BRENNER</div>
  <div class="recipient-address">
    Immobilien Haller &amp; Brenner GbR<br>
    Lindenweg 8
    <div class="city">86999 Musterhausen</div>
  </div>
</section>

</body>
</html>
```